Web Header needed for an inspirational coaching company's website - ongoing work

We need a beautifully designed web header to replace my current one at my homepage on my website www.brekavol.com
There will be continuous work required for various creative work in the future if your work is selected.
I work with corporate professionals and executives to bring clarity and joy back to their career. It needs to be elegant, sophisticated, intelligent, but friendly and inspiring at the same time.
Brief and the sample header size are attached in my files
Thank you!
Target Market(s)
Corporate profesionals and executives
Industry/Entity Type
It Company
Colors
Designer to choose colors to be used in the design.
Look and feel
Each slider illustrates characteristics of the customer's brand and the style your logo design should communicate.

```html
<!DOCTYPE html>
<html lang="en">
<head>
<meta charset="utf-8">
<title>Bright Summit – Your Career Partner header options</title>
<link href="https://fonts.googleapis.com/css2?family=Lato:wght@400;700&family=Yellowtail&display=swap" rel="stylesheet">
<style>
  :root {
    --page-bg: #ffffff;
    --ink: #1b1530;
    --nav-ink: #2a2230;
    --logo-ink: #ffffff;
    --warm-sky-left: #d9dde0;
    --warm-sky-mid: #f6d9a4;
    --warm-sun: #ffe27a;
    --warm-sky-right: #e98c3c;
    --warm-land: #c9662e;
    --warm-land-dark: #8a4a35;
    --warm-water: #e8c9b5;
    --warm-portrait: #c98a6a;
    --cool-sky-left: #5fb2e6;
    --cool-sky-mid: #f2eef3;
    --cool-sun: #fff6ea;
    --cool-sky-right: #b78ab8;
    --cool-land: #a56b99;
    --cool-land-dark: #4c4b8a;
    --cool-water: #d9d0e6;
    --cool-portrait: #6c74b8;
  }
  * { margin: 0; padding: 0; box-sizing: border-box; }
  html, body {
    width: 1200px; height: 1200px; overflow: hidden;
    background: var(--page-bg);
  }
  .canvas { position: relative; width: 1200px; height: 1200px; }

  .header-banner {
    position: absolute; left: 18px; width: 1164px; height: 400px; overflow: hidden;
  }
  .header-banner--warm { top: 144px; }
  .header-banner--cool { top: 600px; }

  .landscape { position: absolute; inset: 0; }
  .header-banner--warm .landscape {
    background:
      radial-gradient(ellipse 320px 200px at 830px 90px, var(--warm-sun), transparent 70%),
      linear-gradient(180deg, transparent 0 50%, var(--warm-land-dark) 62%, var(--warm-land) 75%, var(--warm-water) 88%, #f4e6da 100%),
      linear-gradient(90deg, var(--warm-sky-left) 0%, var(--warm-sky-mid) 45%, #f6c06a 75%, var(--warm-sky-right) 100%);
  }
  .header-banner--cool .landscape {
    background:
      radial-gradient(ellipse 320px 200px at 830px 100px, var(--cool-sun), transparent 70%),
      linear-gradient(180deg, transparent 0 50%, var(--cool-land-dark) 62%, var(--cool-land) 75%, var(--cool-water) 88%, #eef0f6 100%),
      linear-gradient(90deg, var(--cool-sky-left) 0%, var(--cool-sky-mid) 45%, #e6c6d8 75%, var(--cool-sky-right) 100%);
  }

  .portrait {
    position: absolute; left: 90px; top: 82px; width: 240px; height: 318px;
    border-radius: 120px 120px 0 0;
  }
  .header-banner--warm .portrait { background: linear-gradient(180deg, #4a3228 0%, var(--warm-portrait) 45%, #e8602a 100%); }
  .header-banner--cool .portrait { background: linear-gradient(180deg, #1d2a6b 0%, var(--cool-portrait) 45%, #e0605a 100%); }

  .brand {
    position: absolute; left: 180px; top: 26px;
    font-family: "Lato", sans-serif; font-weight: 400;
    font-size: 15px; letter-spacing: 2px; line-height: 1.1;
    color: var(--logo-ink); text-align: center; width: 110px;
  }

  .main-nav {
    position: absolute; left: 342px; top: 32px;
    display: flex; gap: 13px;
    font-family: "Lato", sans-serif; font-weight: 400;
    font-size: 10px; color: var(--nav-ink); letter-spacing: 0.1px;
    list-style: none;
  }

  .hero {
    position: absolute; left: 390px; top: 150px;
    display: flex; flex-direction: column; align-items: flex-end;
    color: var(--ink);
  }
  .hero-title {
    font-family: "Yellowtail", cursive; font-weight: 400;
    font-size: 80px; line-height: 82px;
    white-space: nowrap;
  }
  .hero-tagline {
    margin-top: 6px; padding-right: 50px;
    font-family: "Lato", sans-serif; font-weight: 400;
    font-size: 22px; line-height: 26px; letter-spacing: 2.4px;
    white-space: nowrap;
  }
</style>
</head>
<body>
<main class="canvas">

  <section class="header-banner header-banner--warm">
    <div class="landscape" role="img" aria-label="Sunset over snowy mountains reflected in a calm lake, warm orange tones"></div>
    <div class="portrait" role="img" aria-label="Portrait of the coach smiling, wearing an orange top"></div>
    <div class="brand">BRIGHT SUMMIT</div>
    <ul class="main-nav">
      <li>HOME</li><li>ABOUT LIA MOREN</li><li>TESTIMONIAL</li><li>METHODOLOGY</li>
      <li>COACHING &amp; MENTORING</li><li>WORKSHOP</li><li>CORPORATE</li><li>BLOG</li><li>CONTACT</li>
    </ul>
    <div class="hero">
      <h1 class="hero-title">Your Career Partner</h1>
      <p class="hero-tagline">BRING CLARITY TO YOUR CAREER</p>
    </div>
  </section>

  <section class="header-banner header-banner--cool">
    <div class="landscape" role="img" aria-label="Snowy mountains reflected in a calm lake under a soft sky, cool blue and violet tones"></div>
    <div class="portrait" role="img" aria-label="Portrait of the coach smiling, in cool blue toning"></div>
    <div class="brand">BRIGHT SUMMIT</div>
    <ul class="main-nav">
      <li>HOME</li><li>ABOUT LIA MOREN</li><li>TESTIMONIAL</li><li>METHODOLOGY</li>
      <li>COACHING &amp; MENTORING</li><li>WORKSHOP</li><li>CORPORATE</li><li>BLOG</li><li>CONTACT</li>
    </ul>
    <div class="hero">
      <h1 class="hero-title">Your Career Partner</h1>
      <p class="hero-tagline">BRING CLARITY TO YOUR CAREER</p>
    </div>
  </section>

</main>
</body>
</html>
```